Criação de Layout para Website para alimenticio
" A Ve Brinola é uma empresa que produz doces finos para eventos (corporativos e sociais), cujo público alvo são consumidores que valorizam um produto de qualidade e diferenciado. "

```html
<!DOCTYPE html>
<html lang="pt-BR">
<head>
<meta charset="utf-8">
<title>Ve Brinola — Quem Somos</title>
<link rel="stylesheet" href="https://fonts.googleapis.com/css2?family=Open+Sans:wght@400;600;700&family=Source+Sans+3:wght@400;600&display=swap">
<style>
:root{
  --brown:#6b6157;
  --brown-dark:#564d44;
  --text-brown:#5e5449;
  --sky:#c8eaec;
  --sky-muted:#b9d8da;
  --page:#f7f7f7;
  --line:#c9c6c2;
  --white:#ffffff;
  --footer-a:#6f6a5e;
  --footer-b:#575248;
}
*{margin:0;padding:0;box-sizing:border-box}
html,body{width:927px;height:1200px;overflow:hidden;background:var(--white)}
body{position:relative;font-family:"Source Sans 3",sans-serif;color:var(--text-brown)}
.abs{position:absolute}

/* header */
.social{top:56px;left:780px;display:flex;gap:5px}
.social span{width:32px;height:32px;border-radius:50%;background:#4a423b;display:block}
.search{top:95px;left:699px;width:223px;height:22px;background:#e6e6e6;border-radius:2px}
.search-btn{position:absolute;right:0;top:0;width:26px;height:22px;background:var(--brown-dark);border-radius:0 2px 2px 0}
.search-btn svg{position:absolute;left:7px;top:5px}

.nav{top:128px;left:0;width:927px;height:39px;background:var(--brown)}
.nav a{position:absolute;top:0;height:39px;line-height:39px;font-family:"Open Sans",sans-serif;font-weight:700;font-size:15px;color:var(--white);text-decoration:none;text-align:center;letter-spacing:-.2px}
.nav .menu-icon{position:absolute;left:19px;top:11px}
.nav .home{left:60px;width:93px}
.nav .about{left:153px;width:135px;background:var(--sky);color:var(--brown-dark)}
.nav .products{left:691px;width:124px;border-left:1px solid #7d736a}
.nav .contact{left:815px;width:110px;border-left:1px solid #7d736a}
.brand{top:124px;left:318px;width:296px;height:50px;background:var(--white);text-align:center;font-family:"Open Sans",sans-serif;font-weight:700;font-size:34px;line-height:50px;color:var(--brown-dark);letter-spacing:-.5px}

/* main panel */
.panel{top:172px;left:1px;width:925px;height:814px;background:var(--page);border:1px solid #e6e6e6}
.thumb{left:11px;width:282px}
.t1{top:183px;height:71px;background:linear-gradient(90deg,#6b3a1f,#d9d2c4 50%,#7a3d1c)}
.t2{top:259px;height:71px;background:linear-gradient(90deg,#4a3d38,#9c8f8a 35%,#b45f8a 70%,#4a3a3a)}
.t3{top:337px;height:72px;background:linear-gradient(90deg,#efe8e0,#e08b36 50%,#f3ede4)}
.t4{top:416px;height:72px;background:linear-gradient(90deg,#3a2d22,#e6a234 45%,#d89a30)}
.t5{top:497px;height:71px;background:linear-gradient(90deg,#c5d07c,#e7dccc 30%,#d84d86 60%,#c9a24c)}

.slider{top:182px;left:301px;width:616px;height:386px;background:radial-gradient(ellipse at 55% 45%,#a83040 0%,#6a3a3e 45%,#564c4c 100%)}
.caption{top:376px;left:301px;width:616px;height:141px;background:rgba(30,28,28,.72)}
.caption h2{position:absolute;left:15px;top:7px;font-family:"Source Sans 3",sans-serif;font-weight:400;font-size:27px;color:var(--white);letter-spacing:-.3px}
.caption p{position:absolute;left:15px;top:52px;width:560px;font-size:12.6px;line-height:20px;color:#e8e4e0}
.caption .more{position:absolute;left:13px;top:99px;width:87px;height:30px;background:var(--sky);color:var(--brown-dark);font-size:12px;font-weight:600;line-height:30px;text-align:center;border-radius:2px}
.dots{position:absolute;right:16px;top:125px;display:flex;gap:6px}
.dots i{width:9px;height:9px;border-radius:50%;border:1.5px solid var(--white);display:block}
.dots i.on{background:var(--white)}

.divider{top:604px;left:14px;width:900px;height:1px;background:var(--line)}
.about-title{top:633px;left:29px;font-family:"Open Sans",sans-serif;font-weight:700;font-size:20px;letter-spacing:.6px;color:var(--text-brown)}
.about-logo{top:677px;left:23px;width:186px;height:175px;background:var(--white);border:1px solid #ececec;display:flex;align-items:center;justify-content:center}
.about-logo span{font-family:"Open Sans",sans-serif;font-weight:700;font-size:22px;color:var(--brown-dark)}
.about-text{top:645px;left:220px;width:662px;font-size:17px;line-height:17.3px;text-align:justify;color:var(--text-brown)}
.about-text p{margin-bottom:10px}
.about-text .indent{text-indent:20px}
.about-text em{font-style:italic;font-weight:600}

/* footer */
.footer-band{top:997px;left:0;width:927px;height:8px;background:var(--sky)}
.footer{top:1005px;left:0;width:927px;height:195px;background:linear-gradient(180deg,var(--footer-a),var(--footer-b))}
.col{top:0}
.col svg{position:absolute}
.col h3{position:absolute;top:81px;font-family:"Open Sans",sans-serif;font-weight:700;font-size:24px;color:var(--sky);white-space:nowrap;letter-spacing:-.2px}
.col p{position:absolute;top:107px;font-size:15.5px;line-height:17.5px;color:var(--white);white-space:nowrap}
.col .small{font-size:13.5px;line-height:16px}
.btn{position:absolute;height:19px;background:var(--sky);color:var(--brown-dark);font-size:10px;line-height:19px;text-align:center;border-radius:2px}
.news-input{position:absolute;left:734px;top:125px;width:129px;height:18px;background:#e9e9e9}
</style>
</head>
<body>

<div class="abs social" aria-label="Redes sociais">
  <span></span><span></span><span></span><span></span>
</div>
<div class="abs search">
  <div class="search-btn"><svg width="12" height="12" viewBox="0 0 12 12"><circle cx="5" cy="5" r="3.5" fill="none" stroke="#fff" stroke-width="1.6"/><line x1="7.5" y1="7.5" x2="11" y2="11" stroke="#fff" stroke-width="2"/></svg></div>
</div>

<nav class="abs nav">
  <svg class="menu-icon" width="22" height="17" viewBox="0 0 22 17"><rect y="0" width="22" height="3" fill="#fff"/><rect y="7" width="22" height="3" fill="#fff"/><rect y="14" width="22" height="3" fill="#fff"/></svg>
  <a class="home">HOME</a>
  <a class="about">QUEM SOMOS</a>
  <a class="products">PRODUTOS</a>
  <a class="contact">CONTATO</a>
</nav>
<div class="abs brand">Ve Brinola</div>

<main class="abs panel"></main>

<div class="abs thumb t1" role="img" aria-label="Mesa de festa com bolo branco e flores"></div>
<div class="abs thumb t2" role="img" aria-label="Bandeja de doces decorados em branco e rosa"></div>
<div class="abs thumb t3" role="img" aria-label="Doces com physalis e chocolate branco"></div>
<div class="abs thumb t4" role="img" aria-label="Copinhos de doce de maracujá em bandeja"></div>
<div class="abs thumb t5" role="img" aria-label="Macarons coloridos"></div>

<div class="abs slider" role="img" aria-label="Doces finos com cerejas em bandeja de vidro"></div>
<div class="abs caption">
  <h2>SEJA BEM VINDO !</h2>
  <p>Temos nossa linha fixa, no entanto produzimos doces personalizados para dar um toque exclusivo para o seu evento. Confira nossa linha de produtos.</p>
  <div class="more">SAIBA MAIS</div>
  <div class="dots"><i></i><i class="on"></i><i></i></div>
</div>

<div class="abs divider"></div>
<h1 class="abs about-title">QUEM SOMOS?</h1>
<div class="abs about-logo"><span>Ve Brinola</span></div>
<div class="abs about-text">
  <p class="indent">A <em>Ve Brinola</em> é comandada por Marina Lobato, formada em Gastronomia pelo Instituto Paulista de Culinária e com diversos cursos de especialização em São Paulo e, especificamente em macarons, pela Escola Lumière de Paris e Atelier de Cuisine Valmont.</p>
  <p>O nosso portfólio inclui macarons, chocolates belgas, brigadeiros gourmet, doces finos, bem casados, bolos artísticos, stolens, produtos diet, além das linhas sazonais e doces personalizados. Produzimos também bolos e doces para tornar aquele chá da tarde ainda mais delicioso!</p>
  <p>Os produtos da empresa fizeram parte de eventos corporativos para diversas empresas e adoçaram eventos sociais de renomados espaços.</p>
  <p>Todos os nossos produtos são elaborados através de cuidado processo e os ingredientes primam pela qualidade, originando assim um produto final que busca a excelência e a diferenciação, proporcionando uma experiência gastronômica inesquecível para superar sempre a expectativa dos nossos clientes.</p>
</div>

<div class="abs footer-band"></div>
<footer class="abs footer" role="img" aria-label="Fundo com mesa de festa decorada">
  <div class="abs col">
    <svg style="left:89px;top:30px" width="50" height="46" viewBox="0 0 50 46"><path d="M3 14 C3 4 47 4 47 14 L47 19 L37 19 L37 13 C30 11 20 11 13 13 L13 19 L3 19 Z" fill="#c8eaec"/><path d="M12 22 L38 22 L46 44 L4 44 Z" fill="#c8eaec"/><circle cx="25" cy="32" r="6" fill="#625c52"/><circle cx="25" cy="32" r="2.5" fill="#c8eaec"/></svg>
    <h3 style="left:33px">Atendimento</h3>
    <p style="left:35px">Fone: (11) 95555-0148<br>contato@vebrinola.com.br</p>
  </div>
  <div class="abs col">
    <svg style="left:330px;top:25px" width="36" height="52" viewBox="0 0 36 52"><path d="M18 1 C8 1 1 9 1 18 C1 30 18 51 18 51 C18 51 35 30 35 18 C35 9 28 1 18 1 Z" fill="#c8eaec"/><circle cx="18" cy="17" r="7" fill="#625c52"/></svg>
    <h3 style="left:273px;color:var(--sky-muted)">Onde Estamos</h3>
    <p style="left:275px;font-size:19px">São Paulo</p>
  </div>
  <div class="abs col">
    <svg style="left:550px;top:26px" width="52" height="52" viewBox="0 0 52 52"><path d="M6 2 L2 8 L40 48 L50 50 L47 40 Z" fill="#c8eaec"/></svg>
    <h3 style="left:516px">Orçamento</h3>
    <p class="small" style="left:517px;top:111px">Solicite um orçamento<br>sem compromisso.</p>
    <div class="btn" style="left:517px;top:147px;width:75px">SOLICITAR</div>
  </div>
  <div class="abs col">
    <svg style="left:758px;top:28px" width="60" height="43" viewBox="0 0 60 43"><rect x="0" y="0" width="60" height="43" rx="4" fill="#c8eaec"/><path d="M6 6 L30 26 L54 6 M6 37 L23 21 M54 37 L37 21" fill="none" stroke="#625c52" stroke-width="4"/></svg>
    <h3 style="left:714px;top:83px">Newslatter</h3>
    <p class="small" style="left:716px;top:112px">Receba nossas novidades</p>
    <svg style="left:715px;top:128px" width="14" height="12" viewBox="0 0 14 12"><path d="M1 5 L7 1 L13 5 L13 11 L1 11 Z" fill="#fff"/><path d="M1 5 L7 9 L13 5" fill="none" stroke="#625c52" stroke-width="1.2"/></svg>
    <div class="news-input"></div>
    <div class="btn" style="left:788px;top:150px;width:75px">CADASTRAR</div>
  </div>
</footer>

</body>
</html>
```